***PLASTIC*** Business Card Design

1 sided business card design
The card will be screen printed on plastic, so colour and fonts must be strong.

Must use the colours in the logo eps attached (Black/Ivory/White). Other colour(s) can be added.

Four (4) examples of how the logo can be printed are included in the logo eps attached.

The business card should highlight the logo. The card will be given to architects, interior designers and builders. It should look sophisticated but also innovative.

Do not cover the whole card with colour as it is important than some of the frosted plastic card is visible.

Be creative.

Target Market(s)

architects, interior designers and builders and wealthy home owners

Industry/Entity Type

Plastic

Requirements
Must have
• Must use the colours in the logo eps attached (Black/Ivory/White). Other colour(s) can be added if necessary.

The font is Square721 ExBT but has been a little thickened. It is not essential that you use this font. The name should be a stronger version of the font than other details.

The card will be printed on PVC - see http://www.voltrap.com.au/pricelistbcardsplastic.php

Final artwork must be print ready. You must use the printing spec at http://www.voltrap.com.au/2011%20PVC-TW.pdf

The actual details to be typeset ono the card are:

Dorian Welch

Mobile: 0412 806133
email: info@halcoworks.com.au
www.halcoworks.com.au

PO Box 53, Brenvale, Vic 3029

Plastering | Rendering | Cornicing

```html
<!DOCTYPE html>
<html lang="en">
<head>
<meta charset="utf-8">
<title>Halco Works – Business Card</title>
<link rel="stylesheet" href="https://fonts.googleapis.com/css2?family=Michroma&family=Jura:wght@500;600&display=swap">
<style>
  :root {
    --stage-light: #8d72d8;
    --stage-mid: #4d3a86;
    --stage-dark: #0b0910;
    --frost-top: rgba(235, 228, 255, 0.42);
    --frost-bottom: rgba(200, 190, 240, 0.30);
    --band: #231f22;
    --brand: #8673c9;
    --white: #ffffff;
    --ivory: #f3efe3;
    --tagline: #3a3050;
  }
  * { margin: 0; padding: 0; box-sizing: border-box; }
  html, body {
    width: 1200px;
    height: 898px;
    overflow: hidden;
  }
  body {
    position: relative;
    background: linear-gradient(128deg, var(--stage-light) 0%, var(--stage-mid) 45%, var(--stage-dark) 100%);
    font-family: "Jura", "Michroma", sans-serif;
  }
  .card {
    position: absolute;
    left: 148px;
    top: 163px;
    width: 905px;
    height: 568px;
    border-radius: 32px;
    background: linear-gradient(160deg, var(--frost-top) 0%, var(--frost-bottom) 100%);
    overflow: hidden;
  }
  .band {
    position: absolute;
    left: 0;
    top: 139px;
    width: 100%;
    height: 290px;
    background: var(--band);
  }
  .brand-name {
    position: absolute;
    left: 32px;
    top: 118px;
    width: 385px;
    font-family: "Michroma", sans-serif;
    font-size: 33px;
    letter-spacing: 1px;
    color: var(--brand);
    white-space: nowrap;
  }
  .contact {
    position: absolute;
    left: 500px;
    top: 38px;
    color: var(--white);
  }
  .contact-name {
    font-family: "Michroma", sans-serif;
    font-size: 30px;
    letter-spacing: 0.5px;
    color: var(--white);
    text-shadow: 0.8px 0 0 var(--white);
    margin-bottom: 18px;
  }
  .contact-list {
    list-style: none;
  }
  .contact-item {
    display: flex;
    align-items: center;
    height: 36px;
    font-size: 26px;
    font-weight: 600;
    color: var(--ivory);
    white-space: nowrap;
  }
  .contact-icon {
    width: 24px;
    height: 24px;
    margin: 0 16px 0 4px;
    flex: none;
  }
  .contact-address {
    margin-top: 16px;
    font-size: 26px;
    font-weight: 600;
    color: var(--ivory);
    white-space: nowrap;
  }
  .tagline {
    position: absolute;
    left: 0;
    top: 498px;
    width: 100%;
    text-align: center;
    font-size: 33px;
    font-weight: 500;
    letter-spacing: 0.5px;
    color: var(--tagline);
  }
</style>
</head>
<body>
  <div class="card">
    <div class="band">
      <div class="brand-name">HALCO WORKS</div>

      <div class="contact">
        <div class="contact-name">Dorian Welch</div>
        <ul class="contact-list">
          <li class="contact-item">
            <svg class="contact-icon" viewBox="0 0 24 24" aria-hidden="true">
              <rect x="7" y="4" width="10" height="17" rx="2" fill="none" stroke="#fff" stroke-width="2"/>
              <rect x="9.5" y="7" width="5" height="5" fill="#fff"/>
              <line x1="10" y1="1" x2="10" y2="4" stroke="#fff" stroke-width="1.6"/>
            </svg>
            0412 806133
          </li>
          <li class="contact-item">
            <svg class="contact-icon" viewBox="0 0 24 24" aria-hidden="true">
              <circle cx="12" cy="12" r="4" fill="none" stroke="#fff" stroke-width="2.2"/>
              <path d="M16 8v5.5a2.5 2.5 0 0 0 5 0V12a9 9 0 1 0-3.5 7.1" fill="none" stroke="#fff" stroke-width="2.2"/>
            </svg>
            info@halcoworks.com.au
          </li>
          <li class="contact-item">
            <svg class="contact-icon" viewBox="0 0 24 24" aria-hidden="true">
              <circle cx="12" cy="12" r="9" fill="none" stroke="#fff" stroke-width="1.8"/>
              <ellipse cx="12" cy="12" rx="4" ry="9" fill="none" stroke="#fff" stroke-width="1.4"/>
              <line x1="3" y1="12" x2="21" y2="12" stroke="#fff" stroke-width="1.4"/>
            </svg>
            www.halcoworks.com.au
          </li>
        </ul>
        <div class="contact-address">PO Box 53, Brenvale, Vic 3029</div>
      </div>
    </div>

    <div class="tagline">Plastering | Rendering | Cornicing</div>
  </div>
</body>
</html>
```